Help create retail shipping website

We need a Squarespace design for our company Tandem Parcel. We are a retail shipping service that offers mailboxes, shipping, notary, and printing services. This store is similar to a QMT store, BoxVane, and Wendle Post. We would like to have help designing our website. I will provide our logo for the website. I would like our website to be professional, but be very inviting.

```html
<!DOCTYPE html>
<html lang="en">
<head>
<meta charset="utf-8">
<title>Tandem Parcel — Mailboxes, Shipping, Notary</title>
<link href="https://fonts.googleapis.com/css2?family=Montserrat:wght@300;400;500;600;700;800&display=swap" rel="stylesheet">
<style>
:root{
  --red:#e8151b;
  --ink:#1b1d24;
  --text:#3a3a3a;
  --muted:#555;
  --gray-band:#ececec;
  --white:#ffffff;
  --rule:#8a8a8a;
}
*{box-sizing:border-box;margin:0;padding:0}
html,body{width:1200px;height:3332px;overflow:hidden;background:var(--white)}
body{position:relative;font-family:"Montserrat",sans-serif;color:var(--text)}
.abs{position:absolute}
a{color:inherit;text-decoration:none}

/* header */
.site-header{position:absolute;left:0;top:0;width:1200px;height:80px;background:var(--white)}
.nav-main{position:absolute;left:102px;top:32px;display:flex;gap:19px;font-size:14px;color:#333}
.brand{position:absolute;top:24px;left:0;width:1200px;text-align:center;font-weight:800;font-size:27px;letter-spacing:.5px;color:var(--red)}
.brand-mark{display:inline-block;width:18px;height:18px;background:var(--red);margin-right:10px;vertical-align:-1px}
.nav-contact{position:absolute;left:890px;top:32px;font-size:14px;color:#333}
.btn{position:absolute;display:flex;align-items:center;justify-content:center;font-weight:700;font-size:14px;letter-spacing:.2px;text-transform:uppercase}
.btn-red{background:var(--red);color:var(--white);border-radius:3px}
.btn-dark{background:var(--ink);color:var(--red);border-radius:3px}
.btn-login{left:996px;top:20px;width:99px;height:40px}

/* hero */
.hero{position:absolute;left:0;top:80px;width:1200px;height:600px;
  background:linear-gradient(100deg,#8a7a6a 0%,#b8a993 22%,#6b4a33 45%,#4a3020 60%,#5c6f8a 75%,#3f2b1f 100%)}
.hero-shade{position:absolute;inset:0;background:rgba(0,0,0,.18)}
.hero-kicker{position:absolute;left:0;width:1200px;top:226px;text-align:center;color:#f2f2f2;font-weight:700;font-size:38px;letter-spacing:.5px}
.hero-brand{position:absolute;left:0;width:1200px;top:278px;text-align:center;color:var(--white);font-weight:800;font-size:44px;letter-spacing:.5px}
.btn-hero{left:534px;top:582px;width:132px;height:39px}

/* services */
.section-title{font-weight:700;font-size:33px;color:var(--ink);letter-spacing:.3px}
.section-title .accent{color:var(--red)}
.services-title{position:absolute;top:748px;left:0;width:1200px;text-align:center}
.service{position:absolute;top:848px;width:260px;text-align:center}
.service-icon{width:74px;height:74px;margin:0 auto;background:linear-gradient(135deg,#1a1a1a 60%,var(--red) 60%);border-radius:6px}
.service h3{margin-top:24px;font-weight:600;font-size:24px;color:var(--ink)}
.service p{margin-top:12px;font-size:13.5px;font-weight:400;line-height:23.5px;color:var(--muted)}
.btn-services{left:502px;top:1090px;width:196px;height:39px}

/* gray band */
.gray-band{position:absolute;left:0;top:1209px;width:1200px;height:1287px;background:var(--gray-band)}
.photo{position:absolute}
.about-photo{left:103px;top:1340px;width:497px;height:482px;background:linear-gradient(90deg,#c79a6d 0%,#8a5b3a 30%,#22407e 55%,#b58b5e 75%,#3b4a5a 100%)}
.card{position:absolute;background:var(--white)}
.about-card{left:553px;top:1340px;width:542px;height:364px}
.card-title{position:absolute;left:47px;font-weight:700;font-size:31px;color:var(--ink)}
.card-title .accent{color:var(--red)}
.about-card .card-title{top:36px}
.about-sub{position:absolute;left:47px;top:86px;font-weight:500;font-size:20px;color:var(--ink)}
.card-body{position:absolute;left:47px;font-size:14px;line-height:24px;color:var(--text)}
.about-card .card-body{top:121px;width:455px}
.btn-read{left:600px;top:1620px;width:125px;height:39px}

.testimonial-photo{left:600px;top:1884px;width:495px;height:481px;background:linear-gradient(110deg,#b9a48c 0%,#5b4c43 35%,#3a3a36 55%,#cbb89c 80%,#e6e1d8 100%)}
.testimonial-card{left:103px;top:1884px;width:542px;height:365px}
.testimonial-card .card-title{left:38px;top:46px}
.testimonial-card .card-body{left:38px;top:102px;width:425px}
.testimonial-card .card-body p+p{margin-top:2px}
.quote-author{position:absolute;left:38px;top:310px;font-weight:600;font-size:15px;color:var(--red)}

/* contact band */
.contact-band{position:absolute;left:0;top:2496px;width:1200px;height:481px;
  background:linear-gradient(90deg,#4d5b3e 0%,#6b7a5c 25%,#8fa0a8 45%,#d8332e 58%,#e9e9ea 75%,#5a6e3a 100%)}
.contact-shade{position:absolute;inset:0;background:linear-gradient(90deg,rgba(0,0,0,.35) 0%,rgba(0,0,0,.1) 45%,rgba(0,0,0,0) 100%)}
.contact-title{position:absolute;left:104px;top:2630px;font-weight:700;font-size:31px;color:var(--white)}
.contact-text{position:absolute;left:102px;top:2682px;width:380px;font-weight:500;font-size:15px;line-height:27.5px;color:var(--white)}
.btn-contact{left:102px;top:2795px;width:132px;height:38px}

/* footer */
.footer-brand{position:absolute;left:168px;top:3050px;font-weight:800;font-size:27px;color:var(--red)}
.footer-info{position:absolute;left:167px;font-size:14px;line-height:22px;color:#333}
.footer-col{position:absolute;top:3049px}
.footer-col h4{font-weight:700;font-size:20px;color:var(--ink);margin-bottom:14px;letter-spacing:.2px}
.footer-col li{list-style:none;font-size:14px;line-height:27.5px;color:#333}
.footer-rule{position:absolute;left:103px;top:3277px;width:992px;height:1px;background:var(--rule)}
.copyright{position:absolute;left:0;width:1200px;top:3296px;text-align:center;font-size:14px;color:#333}
</style>
</head>
<body>

<header class="site-header">
  <nav class="nav-main"><a href="#">Home</a><a href="#">About</a><a href="#">Our Services</a><a href="#">Blog</a></nav>
  <div class="brand"><span class="brand-mark"></span>TANDEM PARCEL</div>
  <a class="nav-contact" href="#">Contact Us</a>
  <a class="btn btn-red btn-login" href="#">Log In</a>
</header>

<section class="hero" role="img" aria-label="Courier in a cap handing a parcel to a smiling woman at her front door">
  <div class="hero-shade"></div>
  <h1 class="hero-kicker">WELCOME TO</h1>
  <div class="hero-brand">TANDEM PARCEL</div>
</section>
<a class="btn btn-red btn-hero" href="#">Get Started</a>

<h2 class="section-title services-title"><span class="accent">OUR</span> SERVICES</h2>
<div class="service" style="left:126px">
  <div class="service-icon" role="img" aria-label="Mailbox icon"></div>
  <h3>Mailboxes</h3>
  <p>Lorem ipsum dolor sit amet, consectetur adipiscing elit, sed do eiusmod tempor incididunt dolore magna aliqua.</p>
</div>
<div class="service" style="left:462px">
  <div class="service-icon" role="img" aria-label="Shipping parcel icon with check mark"></div>
  <h3>Shipping</h3>
  <p>Lorem ipsum dolor sit amet, consectetur adipiscing elit, sed do eiusmod tempor incididunt dolore magna aliqua.</p>
</div>
<div class="service" style="left:800px">
  <div class="service-icon" role="img" aria-label="Notary document and pen icon"></div>
  <h3>Notary</h3>
  <p>Lorem ipsum dolor sit amet, consectetur adipiscing elit, sed do eiusmod tempor incididunt dolore magna aliqua.</p>
</div>
<a class="btn btn-dark btn-services" href="#">View More Services</a>

<div class="gray-band"></div>

<div class="photo about-photo" role="img" aria-label="Delivery worker in blue uniform holding a cardboard box"></div>
<section class="card about-card">
  <h2 class="card-title"><span class="accent">ABOUT</span> US</h2>
  <div class="about-sub">Retail Shipping Service</div>
  <p class="card-body">Lorem ipsum dolor sit amet, consectetur adipiscing elit, sed do eiusmod tempor incididunt ut labore et dolore magna aliqua. Quis ipsum suspendisse ultrices gravida. Risus commodo viverra maecenas accumsan lacus vel facilisis. Sed ut perspiciatis unde omnis iste natus error sit voluptatem accusantium doloremque laudantium, totam rem aperiam.</p>
</section>
<a class="btn btn-dark btn-read" href="#">Read More</a>

<div class="photo testimonial-photo" role="img" aria-label="Older man unpacking a parcel at home"></div>
<section class="card testimonial-card">
  <h2 class="card-title"><span class="accent">CLIENT</span> TESTIMONIALS</h2>
  <div class="card-body">
    <p>Lorem ipsum dolor sit amet, consectetur adipiscing elit, sed do eiusmod tempor incididunt ut labore et dolore magna aliqua. Quis ipsum suspendisse ultrices gravida. Risus commodo viverra maecenas accumsan lacus vel facilisis.</p>
    <p>Neque porro quisquam est, qui dolorem ipsum quia dolor sit amet, consectetur, adipisci velit, sed quia non numquam eius modi tempora incidunt ut labore et dolore magnam aliquam quaerat voluptatem.</p>
  </div>
  <div class="quote-author">- Mara Ellison</div>
</section>

<section class="contact-band" role="img" aria-label="Red mailbox on a white post in front of a blurred house and lawn">
  <div class="contact-shade"></div>
</section>
<h2 class="contact-title">CONTACT US</h2>
<p class="contact-text">Lorem ipsum dolor sit amet, consectetur adipiscing elit, sed do eiusmod tempor incididunt ut labore et dolore magna aliqua.</p>
<a class="btn btn-red btn-contact" href="#">Get Started</a>

<footer>
  <div class="footer-brand"><span class="brand-mark"></span>TANDEM PARCEL</div>
  <p class="footer-info" style="top:3118px">25, Tandem Parcel Lorem ipsum<br>Sed ut perspiciatis 2580</p>
  <p class="footer-info" style="top:3169px">+1 555 014 2290</p>
  <p class="footer-info" style="top:3200px">info@tandemparcel.com</p>
  <div class="footer-col" style="left:678px">
    <h4>QUICK LINKS</h4>
    <ul><li>Home</li><li>About</li><li>Our Services</li><li>Blog</li><li>Contact Us</li></ul>
  </div>
  <div class="footer-col" style="left:878px">
    <h4>OUR SERVICES</h4>
    <ul><li>Mailboxes</li><li>Shipping</li><li>Notary</li><li>Printing Services</li></ul>
  </div>
  <div class="footer-rule"></div>
  <div class="copyright">© 2024&nbsp; Tandem Parcel | All rights reserved</div>
</footer>

</body>
</html>
```